Design our Security Warning Sticker to deter thefts and promote our business

Warning sticker to be a deterrent on our customer sites but also do a little advertising for our services at the same time

Create a STANDOUT DESIGN design that will be a deterrent but it will also be promotional for our business services.

We are looking for something that will be bright using our colours as attached. It will not be the same as all other security warning signs but it will be a great design that will demand attention and be easily read without having to much rubbish writing. Should easy to see and the number and website should be clear to see. We may use our website www.guardlyne.co.nz

Target Market(s)

Commercial, Government, residential

Industry/Entity Type

Security

Requirements
Must have
• WARNING
• PROTECTED BY (or something like this)
• LOGO
• 0800 457 216
• ALARMS, ACCESS CONTROL, CCTV, INTERCOMS, DATA CABLING
Nice to have
• Website: www.vantorix.co

```html
<!DOCTYPE html>
<html lang="en">
<head>
<meta charset="utf-8">
<title>Vantorix Security Warning Sticker</title>
<link href="https://fonts.googleapis.com/css2?family=Anton&family=Lato:wght@300;400;900&display=swap" rel="stylesheet">
<style>
  :root {
    --navy: #0d4a7a;
    --orange: #ef432c;
    --white: #ffffff;
    --ink: #1c1c1c;
    --camera-tone: #17507f;
  }
  html, body {
    margin: 0;
    padding: 0;
    overflow: hidden;
    background: var(--navy);
  }
  .sticker {
    position: relative;
    width: 1200px;
    height: 539px;
    background: var(--navy);
    overflow: hidden;
    font-family: "Lato", sans-serif;
  }
  .alert-field {
    position: absolute;
    left: 20px;
    top: 20px;
    width: 822px;
    height: 362px;
    background: var(--orange);
  }
  .camera-illustration {
    position: absolute;
    left: 588px;
    top: 32px;
    width: 254px;
    height: 186px;
    background: linear-gradient(200deg, var(--camera-tone), rgba(13, 74, 122, 0.75));
    border-radius: 6px;
  }
  .headline {
    position: absolute;
    left: 44px;
    top: 255px;
    margin: 0;
    font-family: "Anton", Impact, sans-serif;
    font-weight: 400;
    font-size: 194px;
    line-height: 1;
    color: var(--white);
    letter-spacing: 0;
    -webkit-text-stroke: 4px var(--navy);
    paint-order: stroke fill;
    white-space: nowrap;
    transform: scaleX(1.19);
    transform-origin: left top;
  }
  .subline {
    position: absolute;
    left: 58px;
    top: 448px;
    margin: 0;
    font-weight: 300;
    font-size: 47px;
    line-height: 1;
    letter-spacing: 15px;
    color: var(--white);
    white-space: nowrap;
  }
  .subline .accent {
    color: var(--orange);
  }
  .info-panel {
    position: absolute;
    left: 882px;
    top: 18px;
    width: 299px;
    height: 502px;
    background: var(--white);
    text-align: center;
  }
  .services {
    margin: 14px 0 0;
    font-weight: 400;
    font-size: 14.5px;
    line-height: 20px;
    color: var(--ink);
    white-space: nowrap;
  }
  .services-line {
    display: block;
  }
  .services-line--wide {
    letter-spacing: 2.2px;
  }
  .services-line--tight {
    letter-spacing: 0.2px;
  }
  .protected-by {
    position: absolute;
    left: -20px;
    top: 206px;
    width: 339px;
    margin: 0;
    font-weight: 300;
    font-size: 29px;
    line-height: 1;
    letter-spacing: 7px;
    text-indent: 7px;
    color: var(--ink);
    white-space: nowrap;
  }
  .brand {
    position: absolute;
    left: 0;
    top: 242px;
    width: 100%;
    height: 40px;
    display: flex;
    justify-content: center;
    align-items: center;
    gap: 10px;
  }
  .brand-mark {
    width: 30px;
    height: 30px;
    background: var(--orange);
  }
  .brand-name {
    font-weight: 900;
    font-size: 40px;
    line-height: 1;
    color: var(--navy);
    white-space: nowrap;
  }
  .contact {
    position: absolute;
    left: 0;
    top: 450px;
    width: 100%;
    color: var(--navy);
    font-weight: 300;
    white-space: nowrap;
  }
  .contact-phone {
    display: block;
    font-size: 27px;
    line-height: 24px;
  }
  .contact-web {
    display: block;
    font-size: 25px;
    line-height: 24px;
  }
</style>
</head>
<body>
  <main class="sticker">
    <div class="alert-field"></div>
    <div class="camera-illustration" role="img" aria-label="Illustration of a wall-mounted CCTV security camera"></div>
    <h1 class="headline">WARNING</h1>
    <p class="subline">THIS SITE IS <span class="accent">SECURED</span></p>

    <aside class="info-panel">
      <p class="services">
        <span class="services-line services-line--wide">ALARMS, ACCESS CONTROL,</span>
        <span class="services-line services-line--tight">CCTV, INTERCOMS, DATA CABLING</span>
      </p>
      <p class="protected-by">PROTECTED BY</p>
      <div class="brand">
        <span class="brand-mark"></span>
        <span class="brand-name">VANTORIX</span>
      </div>
      <div class="contact">
        <span class="contact-phone">0800 457 216</span>
        <span class="contact-web">www.vantorix.co</span>
      </div>
    </aside>
  </main>
</body>
</html>
```